Business Card Design

I need a business card design. I am a sole practitioner.I am a psychotherapist and I need a professional card. I am also an art therapist (a form of psychotherapy using art) so I want the image to be professional/creative/maybe ethnic. I do not want a boring minimalist "medical" image, nor do I want it too hippy/tree hugging.
Colours like reds/ochres/yellows would be good.
Contact Information for Business Card
Mira Hask
Psychotherapy, Counselling and Art Therapy
Wunnara Lodge Counselling and Wellbeing services
17 Pellow Road, Toowong 4066
0417639052 www.MiraHask.com.au
on rear of card I need the option to have at least 4 or 5 appointment times /dates

```html
<!DOCTYPE html>
<html lang="en">
<head>
<meta charset="utf-8">
<title>Mira Hask – Business Card</title>
<link rel="stylesheet" href="https://fonts.googleapis.com/css2?family=Roboto+Condensed:wght@700&family=Source+Sans+3:wght@400&display=swap">
<style>
  :root {
    --page: #ffffff;
    --band: #030303;
    --gold-light: #d6c699;
    --gold-mid: #c9ab63;
    --gold-deep: #b98f2c;
    --gold-back: #bb9232;
    --gold-back-soft: #c39d40;
    --ink: #0d0a05;
    --ornament: #2a2114;
  }
  * { margin: 0; padding: 0; box-sizing: border-box; }
  html, body { width: 1200px; height: 741px; overflow: hidden; background: var(--page); }
  .canvas { position: relative; width: 1200px; height: 741px; background: var(--page); }
  .stage-band { position: absolute; left: 0; top: 563px; width: 1200px; height: 178px; background: var(--band); }

  .card { position: absolute; top: 114px; width: 583px; height: 359px; overflow: hidden; }
  .card--front {
    left: 13px;
    background: radial-gradient(ellipse 60% 75% at 50% 28%, var(--gold-light) 0%, var(--gold-mid) 55%, var(--gold-deep) 100%);
    color: var(--ink);
    text-align: center;
  }
  .card--back {
    left: 604px;
    background: radial-gradient(ellipse 80% 90% at 50% 50%, var(--gold-back-soft) 0%, var(--gold-back) 100%);
    color: var(--ink);
  }

  .ornament { position: absolute; top: 104px; width: 120px; height: 151px; }
  .ornament--left { left: 2px; }
  .ornament--right { right: 0; }

  .practitioner-name {
    position: absolute; left: 0; right: 0; top: 140px;
    font-family: "Roboto Condensed", "Arial Narrow", sans-serif;
    font-weight: 700; font-size: 50px; line-height: 1; letter-spacing: -0.5px;
  }
  .practitioner-services {
    position: absolute; left: 0; right: 0; top: 196px;
    font-family: "Source Sans 3", "Myriad Pro", sans-serif; font-size: 17px;
  }
  .practice-details {
    position: absolute; left: 0; right: 0; top: 287px;
    font-family: "Source Sans 3", "Myriad Pro", sans-serif; font-size: 17px; line-height: 21.5px;
  }
  .practice-details p { margin: 0; }

  .appointment-divider { position: absolute; left: 284px; top: 0; width: 3px; height: 359px; background: var(--ink); }
  .appointment-heading {
    position: absolute; left: 112px; top: 14px;
    font-family: "Source Sans 3", "Myriad Pro", sans-serif; font-size: 21px;
    display: flex; align-items: baseline;
  }
  .appointment-heading .rule { display: inline-block; width: 262px; border-bottom: 2px solid var(--ink); margin: 0 1px; }
  .appointment-line { position: absolute; height: 0; border-bottom: 3px dotted var(--ink); }
  .appointment-line--time { left: 65px; width: 213px; }
  .appointment-line--date { left: 293px; width: 233px; }
</style>
</head>
<body>
<div class="canvas">
  <section class="card card--front" aria-label="Business card front">
    <svg class="ornament ornament--left" viewBox="0 0 120 151" role="img" aria-label="Black spiral ornament cluster pointing inward">
      <polygon points="0,0 120,75.5 0,151" fill="var(--ornament)"/>
    </svg>
    <svg class="ornament ornament--right" viewBox="0 0 120 151" role="img" aria-label="Black spiral ornament cluster pointing inward">
      <polygon points="120,0 0,75.5 120,151" fill="var(--ornament)"/>
    </svg>
    <h1 class="practitioner-name">Mira Hask</h1>
    <p class="practitioner-services">Psychotherapy | Counselling | Art Therapy</p>
    <div class="practice-details">
      <p class="practice-name">Wunnara Lodge Counselling &amp; Wellbeing Services</p>
      <p class="practice-address">17 Pellow Road, Kelmore 4071&nbsp; |&nbsp; 0417 639052</p>
      <p class="practice-web">www.MiraHask.com.au</p>
    </div>
  </section>

  <section class="card card--back" aria-label="Business card back with appointment time and date slots">
    <div class="appointment-divider"></div>
    <div class="appointment-heading"><span>TIME</span><span class="rule"></span><span>DATE</span></div>
    <div class="appointment-line appointment-line--time" style="top:86px"></div>
    <div class="appointment-line appointment-line--date" style="top:86px"></div>
    <div class="appointment-line appointment-line--time" style="top:140px"></div>
    <div class="appointment-line appointment-line--date" style="top:140px"></div>
    <div class="appointment-line appointment-line--time" style="top:194px"></div>
    <div class="appointment-line appointment-line--date" style="top:194px"></div>
    <div class="appointment-line appointment-line--time" style="top:248px"></div>
    <div class="appointment-line appointment-line--date" style="top:248px"></div>
    <div class="appointment-line appointment-line--time" style="top:302px"></div>
    <div class="appointment-line appointment-line--date" style="top:302px"></div>
  </section>

  <div class="stage-band"></div>
</div>
</body>
</html>
```